Meadowbrook Clinical Trials Redesign

Website name: http://meadowbrookclinicaltrials.example/live/
Industry: medical & pharmaceutical
Target audience:
Clinical research patients
clinical research sponsors
clinical research referring doctors
Style/theme of your website design:
We want to customize the corvid theme, emulating our competitors website
http://layoutbazaar.example/item/corvid-responsive-multipurpose-wordpress-theme/4172305
Webdesign Examples?
http://www.jpnclinical.example/currently-enrolling-clinical-trials/
https://www.tundrastudies.example/
What do you like about these sites:
These sites address all the needs of a clinical trial facility. The patient, the doctor and the sponsor. Also they have forms and sign up information for each trial they offer. The site needs to have SCHEMA markup and rich snippets. We have reviews and testimonial that need schema markup also, local NAP information and all the other rich snippet markups available.
How many pages need design:
8-12
List any colors:
existing color of website and logo
Target Market(s)
Target audience:
Industry/Entity Type
Pharmaceutical
Number of Pages Required
5+ page

```html
<!DOCTYPE html>
<html lang="en">
<head>
<meta charset="utf-8">
<title>Meadowbrook Clinical Trials</title>
<link rel="stylesheet" href="https://fonts.googleapis.com/css2?family=Raleway:wght@300;400;500;600;700&family=Open+Sans:wght@400;600;700&family=Oswald:wght@300;400&display=swap">
<style>
:root{
  --teal:#1cb0a5;
  --teal-dark:#13968c;
  --teal-deep:#0f7f7a;
  --ink:#2b2b2b;
  --text:#555;
  --muted:#888;
  --band:#f4f4f4;
  --line:#e2e2e2;
  --gold:#e0a526;
  --footer:#262626;
  --footer-base:#1b1b1b;
  --white:#fff;
}
*{box-sizing:border-box;margin:0;padding:0}
html,body{width:1200px;height:3000px;overflow:hidden;background:var(--white)}
body{font-family:"Open Sans",Arial,sans-serif;color:var(--text);position:relative}
.canvas{position:relative;width:1200px;height:3000px;overflow:hidden}
.abs{position:absolute}

/* header */
.site-header{top:0;left:0;width:1200px;height:132px;background:var(--white)}
.brand{left:100px;top:30px;display:flex;align-items:center;gap:16px}
.brand-mark{width:64px;height:64px;border-radius:50%;background:var(--teal)}
.brand-name{font-family:"Raleway",sans-serif;font-weight:600;font-size:28px;line-height:30px;color:var(--teal);width:220px}
.contact-top{left:860px;top:42px;display:flex;gap:16px;align-items:center}
.phone-ring{width:42px;height:42px;border:2px solid #444;border-radius:50%;display:flex;align-items:center;justify-content:center}
.contact-top .ph{font-family:"Raleway",sans-serif;font-size:19px;color:#333;font-weight:500}
.contact-top .em{font-size:14px;color:#555;margin-top:4px}

/* nav */
.main-nav{top:132px;left:0;width:1200px;height:56px;background:linear-gradient(#22bdb1,var(--teal-dark))}
.main-nav ul{list-style:none;display:flex;height:56px;padding-left:98px}
.main-nav li{font-family:"Raleway",sans-serif;font-size:13px;font-weight:600;color:var(--white);height:56px;line-height:56px;padding:0 21px;letter-spacing:.3px}
.main-nav li.active{background:#e9ecea;color:var(--teal);padding:0 24px}

/* hero */
.hero{top:188px;left:0;width:1200px;height:562px;background:linear-gradient(100deg,#5f8ea4 0%,#a9c7d6 45%,#d7e3ea 70%,#8aa9b8 100%)}
.hero-mark{left:130px;top:360px;width:120px;height:120px;border-radius:50%;background:rgba(28,176,165,.85)}
.hero-title{left:266px;top:354px;font-family:"Raleway",sans-serif;font-weight:700;font-size:40px;line-height:58px;color:var(--white);letter-spacing:1px}
.hero-lead{left:130px;top:474px;font-family:"Raleway",sans-serif;font-weight:600;font-size:21px;line-height:30px;color:var(--white);width:520px}
.btn-ghost{border:2px solid rgba(255,255,255,.8);color:var(--white);font-family:"Raleway",sans-serif;font-weight:600;font-size:18px;display:flex;align-items:center;justify-content:center;letter-spacing:.5px}
.hero-btn{left:130px;top:548px;width:216px;height:48px;border-radius:4px}
.slide-arrow{width:34px;height:34px;border-radius:50%;background:rgba(0,0,0,.35);display:flex;align-items:center;justify-content:center}

/* intro band */
.intro-band{top:750px;left:0;width:1200px;height:110px;background:var(--band);text-align:center}
.intro-band h2{font-family:"Raleway",sans-serif;font-weight:400;font-size:34px;color:var(--teal);margin-top:14px}
.intro-band p{font-size:15px;color:#333;margin-top:4px}
.band-notch{top:858px;left:560px}

/* services */
.service{top:940px;width:236px;height:286px;text-align:center;padding-top:22px}
.service.featured{border:1px solid var(--line)}
.svc-icon{width:100px;height:100px;border:3px solid var(--teal);border-radius:50%;margin:0 auto;display:flex;align-items:center;justify-content:center}
.service h3{font-family:"Raleway",sans-serif;font-weight:400;font-size:17px;color:#333;margin-top:30px}
.service p{font-size:12px;line-height:21px;color:#555;margin:10px 14px 0}
.service .more{font-size:13px;color:#555;margin-top:14px;display:block}

/* participate */
.participate{top:1278px;left:0;width:1200px;height:402px;background:linear-gradient(110deg,#1cb3a7 0%,#22b8ad 55%,#3bb8b4 100%)}
.participate h2{position:absolute;left:100px;top:72px;font-family:"Raleway",sans-serif;font-weight:700;font-size:30px;color:var(--white)}
.participate .copy{position:absolute;left:100px;top:128px;width:606px;font-size:12px;line-height:21px;color:var(--white)}
.participate .copy p+p{margin-top:12px}
.future-art{left:760px;top:1390px;width:220px;height:182px;border-radius:10px;background:linear-gradient(160deg,#6fcfe0,#1a2b38 70%)}
.future-tag{left:994px;top:1430px;font-family:"Raleway",sans-serif;color:var(--white);line-height:1}
.future-tag .sm{font-size:22px;font-weight:500}
.future-tag .lg{font-size:38px;font-weight:500}

/* expect */
.device-art{left:100px;top:1748px;width:442px;height:362px;border-radius:8px;background:linear-gradient(180deg,#2a2a2a 0 6%,#bfd2de 6% 74%,#e6e6e6 74% 86%,#c7c7c7 86%)}
.expect-title{left:588px;top:1744px;font-family:"Raleway",sans-serif;font-weight:400;font-size:30px;line-height:38px;color:#222;width:460px}
.expect-copy{left:588px;top:1828px;width:512px;font-size:11px;line-height:21px;color:#333}
.checklist{left:588px;top:1956px;width:512px;list-style:none}
.checklist li{height:34px;border-bottom:1px solid var(--line);display:flex;align-items:center;gap:14px;font-size:11px;color:#444;letter-spacing:.2px}
.checklist li:last-child{border-bottom:none}
.dot{width:10px;height:10px;border:2px solid var(--gold);border-radius:50%}

/* benefits */
.benefits{top:2160px;left:0;width:1200px;height:456px;background:linear-gradient(180deg,#1d9a9c 0%,#137c80 60%,#0f6f74 100%);text-align:center}
.benefits-mark{position:absolute;left:544px;top:58px;width:112px;height:112px;border-radius:50%;background:rgba(140,225,220,.7)}
.benefits h2{position:absolute;left:0;top:198px;width:1200px;font-family:"Oswald",sans-serif;font-weight:300;font-size:31px;color:var(--white);letter-spacing:.5px}
.benefits p{position:absolute;left:0;top:252px;width:1200px;font-size:15px;line-height:22px;color:var(--white)}
.benefits-btn{left:486px;top:2502px;width:228px;height:50px;border-radius:25px;font-size:19px}

/* footer */
.site-footer{top:2616px;left:0;width:1200px;height:260px;background:var(--footer)}
.f-col{position:absolute;top:46px}
.f-col h4{font-family:"Open Sans",sans-serif;font-weight:400;font-size:14px;color:#ccc;letter-spacing:.5px}
.f-col p{font-size:11px;line-height:20px;color:#8c8c8c;margin-top:14px}
.field{height:42px;border-bottom:1px solid #333;font-size:10px;color:#777;display:flex;align-items:center;padding-left:14px;background:#1f1f1f}
.subscribe{position:absolute;left:164px;top:0;width:100px;height:42px;background:var(--teal);color:var(--white);font-size:12px;display:flex;align-items:center;justify-content:center}
.f-contact{font-size:12px;color:#8c8c8c;line-height:20px}
.f-row{display:flex;gap:18px;align-items:center;margin-top:14px}
.footer-base{top:2876px;left:0;width:1200px;height:124px;background:var(--footer-base);text-align:center}
.footer-base .copy{font-size:11px;color:#8c8c8c;margin-top:34px}
.footer-base .copy b{color:#ccc;font-weight:600}
.socials{display:flex;gap:10px;justify-content:center;margin-top:18px}
.socials span{width:28px;height:28px;border:1px solid #555;border-radius:50%}
</style>
</head>
<body>
<div class="canvas">

  <header class="site-header abs">
    <div class="brand abs">
      <span class="brand-mark"></span>
      <span class="brand-name">Meadowbrook Clinical Trials</span>
    </div>
    <div class="contact-top abs">
      <span class="phone-ring">
        <svg width="18" height="18" viewBox="0 0 24 24"><path d="M6.6 10.8a15 15 0 0 0 6.6 6.6l2.2-2.2a1 1 0 0 1 1-.25 11 11 0 0 0 3.6.6 1 1 0 0 1 1 1V20a1 1 0 0 1-1 1A17 17 0 0 1 3 4a1 1 0 0 1 1-1h3.5a1 1 0 0 1 1 1 11 11 0 0 0 .6 3.6 1 1 0 0 1-.25 1z" fill="#444"/></svg>
      </span>
      <div>
        <div class="ph">Ph: (555) 314-7720</div>
        <div class="em">info@meadowbrookclinicaltrials.example</div>
      </div>
    </div>
  </header>

  <nav class="main-nav abs">
    <ul>
      <li class="active">HOME</li>
      <li>ABOUT US</li>
      <li>CLINICAL TRIALS</li>
      <li>TRIALS</li>
      <li>PARTICIPATE</li>
      <li>FAQS</li>
      <li>SPONSORS</li>
      <li>CONTACT US</li>
    </ul>
  </nav>

  <section class="hero abs" role="img" aria-label="Photo of a senior researcher in a lab coat working with samples in a bright laboratory"></section>
  <span class="hero-mark abs"></span>
  <h1 class="hero-title abs">MEADOWBROOK<br>CLINICAL TRIALS</h1>
  <p class="hero-lead abs">Meadowbrook Clinical Trials Incorporation, is a dedicated research facility founded in 2010</p>
  <a class="btn-ghost hero-btn abs">MORE INFORMATION</a>
  <span class="slide-arrow abs" style="left:38px;top:440px"><svg width="12" height="12" viewBox="0 0 12 12"><path d="M8 1 3 6l5 5" stroke="#fff" stroke-width="2" fill="none"/></svg></span>
  <span class="slide-arrow abs" style="left:1116px;top:440px"><svg width="12" height="12" viewBox="0 0 12 12"><path d="m4 1 5 5-5 5" stroke="#fff" stroke-width="2" fill="none"/></svg></span>

  <section class="intro-band abs">
    <h2>Clinical Trials</h2>
    <p>We provide several services that will help you with your recycling Process</p>
  </section>
  <svg class="band-notch abs" width="80" height="28" viewBox="0 0 80 28"><path d="M0 0h80L40 28z" fill="#f4f4f4"/></svg>

  <article class="service featured abs" style="left:100px">
    <div class="svc-icon"><svg width="50" height="50" viewBox="0 0 50 50" fill="none" stroke="#1cb0a5" stroke-width="3"><path d="M7 34a18 18 0 1 1 36 0z"/><path d="M25 34l8-12"/><path d="M10 40h30"/></svg></div>
    <h3>Weight Loss</h3>
    <p>Lorem ipsum dolor sit amet, consectetuer adipiscing elit. Lorem ipsum Lorem ipsum dolor</p>
    <span class="more">READ MORE</span>
  </article>
  <article class="service abs" style="left:356px">
    <div class="svc-icon"><svg width="50" height="50" viewBox="0 0 50 50" fill="none" stroke="#1cb0a5" stroke-width="3"><circle cx="25" cy="28" r="16"/><path d="M21 6h8M25 6v6"/><path d="M14 29h6l3-6 4 10 3-4h6"/></svg></div>
    <h3>Heart Disease</h3>
    <p>Lorem ipsum dolor sit amet, consectetuer adipiscing elit. Lorem ipsum Lorem ipsum dolor</p>
    <span class="more">READ MORE</span>
  </article>
  <article class="service abs" style="left:612px">
    <div class="svc-icon"><svg width="50" height="50" viewBox="0 0 50 50" fill="none" stroke="#1cb0a5" stroke-width="3"><rect x="15" y="5" width="20" height="32" rx="4"/><rect x="20" y="11" width="10" height="8"/><path d="M25 37v8"/></svg></div>
    <h3>Type II Diabetes</h3>
    <p>Lorem ipsum dolor sit amet, consectetuer adipiscing elit. Lorem ipsum Lorem ipsum dolor</p>
    <span class="more">READ MORE</span>
  </article>
  <article class="service abs" style="left:868px">
    <div class="svc-icon"><svg width="50" height="50" viewBox="0 0 50 50" fill="none" stroke="#1cb0a5" stroke-width="3"><path d="M20 30V8a5 5 0 0 1 10 0v22a9 9 0 1 1-10 0z"/><path d="M25 14v20"/></svg></div>
    <h3>High Cholesterol</h3>
    <p>Lorem ipsum dolor sit amet, consectetuer adipiscing elit. Lorem ipsum Lorem ipsum dolor</p>
    <span class="more">READ MORE</span>
  </article>

  <section class="participate abs">
    <h2>Who Can Participate In A Clinical Trial?</h2>
    <div class="copy">
      <p>All clinical trials have guidelines about who can participate. Before joining a clinical trial, a volunteer must qualify for the study. The factors that allow volunteers to participate in a clinical trial are called "inclusion criteria" and the factors that disallow volunteers from participating are called "exclusion criteria". These criteria can include age, gender, the type of stage of a disease, previous treatment history, and other medical conditions.</p>
      <p>Some research studies seek participants with specific illnesses or conditions to be studied in a clinical trial, while others require healthy participants. It is important to note that inclusion and exclusion criteria are used to identify appropriate participants, promote participant's safety, and ensure that researches learn about information they need.</p>
    </div>
  </section>
  <div class="future-art abs" role="img" aria-label="Illustration of a cartoon character leaning on a tablet showing a map pin and hospital"></div>
  <div class="future-tag abs"><div class="sm">The</div><div class="lg">Future</div><div class="sm">is <span class="lg">Now</span></div></div>

  <div class="device-art abs" role="img" aria-label="Desktop monitor showing a lab researcher in mask and gloves handling samples"></div>
  <h2 class="expect-title abs">What can volunteers expect if they choose to participate?</h2>
  <p class="expect-copy abs">In some studies, participants receive a physical examination and their medical histories are reviewed by either the study physician or a research staff member once they are enrolled in the study. The volunteer's health will continue to be monitored during and after the trial. A detailed description of what's expected of volunteers will be outlined in consent forms along with specific clinical trial information.</p>
  <ul class="checklist abs">
    <li><span class="dot"></span>SED UT PERSPICIATIS UNDE OMNIS ISTE</li>
    <li><span class="dot"></span>ACCUSANTIUM DOLOREMQUE LAUDANT</li>
    <li><span class="dot"></span>ROTAM REM APERIAM EAQUE IPSA UAE</li>
    <li><span class="dot"></span>AILLO INVENTORE VERITATIS ET QUASI</li>
  </ul>

  <section class="benefits abs" role="img" aria-label="Teal-tinted photo of a hospital corridor">
    <span class="benefits-mark"></span>
    <h2>WHAT ARE THE BENEFITS AND RISKS OF JOINING A TRIAL?</h2>
    <p>Volunteers in a clinical trial participate in the development of medical therapies<br>that may offer better treatments and even cures for life-threatening and chronic diseases.<br>However, there are risks involved.</p>
  </section>
  <a class="btn-ghost benefits-btn abs">JOINING A TRIAL</a>
  <span class="slide-arrow abs" style="left:52px;top:2414px"><svg width="12" height="12" viewBox="0 0 12 12"><path d="M8 1 3 6l5 5" stroke="#fff" stroke-width="2" fill="none"/></svg></span>
  <span class="slide-arrow abs" style="left:1114px;top:2414px"><svg width="12" height="12" viewBox="0 0 12 12"><path d="m4 1 5 5-5 5" stroke="#fff" stroke-width="2" fill="none"/></svg></span>

  <footer class="site-footer abs">
    <div class="f-col" style="left:100px;width:320px">
      <h4>SIGN UP FOR NEWSLETTER</h4>
      <p>Excepteur sint occaecat cupidatat non proident, sunt in culpa qui officia deserunt</p>
      <div style="position:relative;margin-top:22px;width:264px">
        <div class="field">Enter Name</div>
        <div style="position:relative;margin-top:8px">
          <div class="field" style="width:164px">Enter Email</div>
          <span class="subscribe">SUBSCRIBE</span>
        </div>
      </div>
    </div>
    <div class="f-col" style="left:470px;width:330px">
      <h4>ABOUT US</h4>
      <p>Lorem ipsum dolor sit amet, consectetur adipiscing elit, sed do eiusmod tempor incididunt ut labore et dolore magna aliqua. Ut enim ad minim veniam, quis nostrud exercitation ullamco laboris nisi ut aliquip ex ea commodo Lorem ipsum dolor sit amet, consectetur adipiscing elit, sed do eiusmod tempor incididunt ut labore</p>
    </div>
    <div class="f-col" style="left:890px;width:240px">
      <h4>CONTACT US</h4>
      <p class="f-contact">2760 Alder Creek Rd. Suite 140<br>Fernvale, CA 90000</p>
      <div class="f-row f-contact"><svg width="16" height="16" viewBox="0 0 24 24"><path d="M6.6 10.8a15 15 0 0 0 6.6 6.6l2.2-2.2a1 1 0 0 1 1-.25 11 11 0 0 0 3.6.6 1 1 0 0 1 1 1V20a1 1 0 0 1-1 1A17 17 0 0 1 3 4a1 1 0 0 1 1-1h3.5a1 1 0 0 1 1 1 11 11 0 0 0 .6 3.6 1 1 0 0 1-.25 1z" fill="none" stroke="#8c8c8c" stroke-width="1.5"/></svg>+(555) 314-7720</div>
      <div class="f-row f-contact" style="margin-top:8px"><svg width="16" height="14" viewBox="0 0 16 14"><rect x="1" y="2" width="14" height="10" fill="none" stroke="#8c8c8c"/><path d="m1 2 7 6 7-6" fill="none" stroke="#8c8c8c"/></svg>info@meadowbrookclinicaltrials.example</div>
    </div>
  </footer>

  <div class="footer-base abs">
    <p class="copy">©2014 - 2015 <b>MEADOWBROOK CLINICAL TRIALS</b>. All Rights Reserved.</p>
    <div class="socials"><span></span><span></span><span></span><span></span><span></span></div>
  </div>

</div>
</body>
</html>
```